Design a Business Card

My customer is a Franchise Consultant.
Please find the current business card design of my customer for the info that will be put on the new card also.
JPG format of his logo ias also attached.
We want a modern business card design for him.
Wanted features:
1) Simple and flat design,
2) Heavy paper (Not folded),
3) Original Cut shape,
4) Partial lacquer printing for logo

```html
<!DOCTYPE html>
<html lang="tr">
<head>
<meta charset="utf-8">
<title>Selim Arkan – Business Card</title>
<link href="https://fonts.googleapis.com/css2?family=Lato:wght@400;700;900&display=swap" rel="stylesheet">
<style>
  :root {
    --backdrop: #6a6a6a;
    --navy: #263648;
    --gold: #fccf0a;
    --gold-text: #f3c623;
    --white: #ffffff;
  }
  * { margin: 0; padding: 0; box-sizing: border-box; }
  html, body {
    width: 1200px;
    height: 1200px;
    overflow: hidden;
    background: var(--backdrop);
    font-family: "Lato", sans-serif;
  }
  .card {
    position: absolute;
    left: 240px;
    width: 720px;
    height: 420px;
    background: var(--navy);
    overflow: hidden;
  }
  .card--front { top: 141px; }
  .card--back { top: 637px; }

  .brand {
    position: absolute;
    text-align: center;
    color: var(--gold-text);
  }
  .brand__name {
    font-weight: 400;
    letter-spacing: 1px;
  }
  .brand__role {
    font-weight: 700;
    text-transform: uppercase;
  }
  .card--front .brand { left: 0; right: 0; top: 140px; }
  .card--front .brand__name { font-size: 54px; line-height: 64px; }
  .card--front .brand__role { font-size: 15px; letter-spacing: 2.6px; margin-top: 10px; }

  .website {
    position: absolute;
    left: 0; right: 0;
    top: 372px;
    text-align: center;
    color: var(--white);
    font-size: 17px;
    letter-spacing: 0.3px;
  }

  .card--back .brand { left: 30px; width: 290px; top: 168px; }
  .card--back .brand__name { font-size: 32px; line-height: 40px; }
  .card--back .brand__role { font-size: 9px; letter-spacing: 1.6px; margin-top: 6px; }

  .back-shape { position: absolute; inset: 0; }

  .person {
    position: absolute;
    right: 26px;
    top: 72px;
    text-align: right;
    color: var(--navy);
  }
  .person__name { font-size: 27px; font-weight: 400; line-height: 30px; }
  .person__name strong { font-weight: 900; }
  .person__title { font-size: 15px; margin-top: 2px; }

  .contact {
    position: absolute;
    right: 79px;
    text-align: right;
    color: var(--navy);
    font-size: 16px;
    line-height: 21px;
  }
  .contact--phone { top: 175px; }
  .contact--mail { top: 252px; }
  .contact--address { top: 328px; }

  .contact-rail { position: absolute; right: 0; top: 0; width: 80px; height: 420px; }
</style>
</head>
<body>

<section class="card card--front">
  <div class="brand">
    <div class="brand__name">Selim Arkan</div>
    <div class="brand__role">Franchise &amp; Marka Danışmanı</div>
  </div>
  <div class="website">urwebsitname.com</div>
</section>

<section class="card card--back">
  <svg class="back-shape" width="720" height="420" viewBox="0 0 720 420">
    <path d="M411 -5 Q 300 210 407 425 L 725 425 L 725 -5 Z" fill="var(--white)"/>
    <path d="M419 -5 Q 308 210 415 425 L 725 425 L 725 -5 Z" fill="var(--gold)"/>
  </svg>

  <div class="brand">
    <div class="brand__name">Selim Arkan</div>
    <div class="brand__role">Franchise &amp; Marka Danışmanı</div>
  </div>

  <div class="person">
    <div class="person__name"><strong>JOHNNY</strong> DEO</div>
    <div class="person__title">Designation</div>
  </div>

  <div class="contact contact--phone">+1233 456 789<br>+1233 456 789</div>
  <div class="contact contact--mail">urmail@mailbox.com<br>urwebsitname.com</div>
  <div class="contact contact--address">ur address gose here<br>ur city zip code 1234</div>

  <svg class="contact-rail" viewBox="0 0 80 420" width="80" height="420">
    <line x1="33" y1="196" x2="33" y2="349" stroke="var(--navy)" stroke-width="3"/>
    <g class="icon icon--phone">
      <circle cx="33" cy="196" r="19" fill="var(--navy)"/>
      <path d="M26 189 q2 -2 4 0 l2 3 q1 2 -1 3 q1 4 5 5 q1 -2 3 -1 l3 2 q2 2 0 4 q-2 2 -5 1 q-9 -3 -12 -12 q-1 -3 1 -5z" fill="var(--white)"/>
      <path d="M36 188 a7 7 0 0 1 6 6 M35 184 a11 11 0 0 1 10 10" fill="none" stroke="var(--white)" stroke-width="1.6"/>
    </g>
    <g class="icon icon--mail">
      <circle cx="33" cy="273" r="19" fill="var(--navy)"/>
      <rect x="23" y="266" width="20" height="14" rx="1.5" fill="none" stroke="var(--white)" stroke-width="2"/>
      <path d="M23 267 L33 275 L43 267" fill="none" stroke="var(--white)" stroke-width="2"/>
    </g>
    <g class="icon icon--pin">
      <circle cx="33" cy="349" r="19" fill="var(--navy)"/>
      <path d="M33 361 C27 353 25 349 25 345 a8 8 0 0 1 16 0 c0 4 -2 8 -8 16z" fill="var(--white)"/>
      <circle cx="33" cy="345" r="3" fill="var(--navy)"/>
    </g>
  </svg>
</section>

</body>
</html>
```